A start-up named "brivora" - a clinical research organization needs a new PowerPoint design

We need a new PowerPoint Design (incl. business card and stationery design) for an early-stage start-up named "brivora" seeking to build an ecosystem/ strategic partner alliances or consortium of committed and active collaborators to guide important components of the clinical trial.

Our ultimate goal is to avoid false neutrals – therapies that have not been and may never be evaluated in clinical trials due to the costs and/ or complexity.

The final design should highlight our patient-centric approach, innovative study design supported with the novel AI platform to make a stronger impact on patient lives.

Please see the attached brief for more details.
Updates

Requesting the proposals on color-coding, business-card designs, clinical research visuals, and icons as well as stationery design.

Target Market(s)

Pharma/ Biotech Executives
Medical Institutions
Clinical Trial Participants (Patients)

Colors
e34398

Requirements
Must have
• Use the Color Version of purple/ magenta logo

```html
<!DOCTYPE html>
<html lang="en">
<head>
<meta charset="utf-8">
<title>brivora – stationery set</title>
<link rel="stylesheet" href="https://fonts.googleapis.com/css2?family=Source+Sans+3:wght@400;600;700&display=swap">
<style>
  :root {
    --brand: #c0196d;
    --brand-bright: #e34398;
    --ink: #2b2b2b;
    --ink-soft: #555a60;
    --paper: #ffffff;
    --paper-tint: #f4f5f6;
    --band-top: #e6e8ea;
    --band-bottom: #f1f2f3;
    --stage: #eceef0;
    --shadow: rgba(0, 0, 0, 0.22);
  }
  * { box-sizing: border-box; margin: 0; padding: 0; }
  html, body { width: 1200px; height: 3650px; overflow: hidden; background: var(--paper); }
  body { position: relative; font-family: "Source Sans 3", sans-serif; color: var(--ink); }

  .icon { width: 20px; height: 20px; fill: var(--brand); flex: none; }
  .wordmark { font-weight: 700; color: var(--brand); letter-spacing: -0.5px; display: flex; align-items: center; gap: 12px; line-height: 1; }
  .wordmark-mark { background: var(--brand); flex: none; }

  .contact-list { list-style: none; }
  .contact-list li { display: flex; align-items: center; }

  /* Business cards */
  .card-stage { position: absolute; left: 0; top: 0; width: 1200px; height: 842px; background: var(--stage); }
  .card { position: absolute; top: 270px; width: 490px; height: 280px; box-shadow: 0 14px 30px var(--shadow); }
  .card-front { left: 85px; background: var(--paper); border-bottom: 8px solid var(--brand); }
  .card-back { left: 625px; background: var(--brand); display: flex; align-items: center; justify-content: center; }
  .card-back .wordmark { color: var(--paper); font-size: 56px; }
  .card-back .wordmark-mark { background: var(--paper); width: 22px; height: 22px; }
  .card-name { position: absolute; left: 40px; top: 70px; font-size: 26px; font-weight: 700; color: var(--ink); }
  .card-role { position: absolute; left: 40px; top: 104px; font-size: 14px; color: var(--brand); }
  .card-divider { position: absolute; left: 250px; top: 60px; width: 2px; height: 150px; background: var(--brand); }
  .card-front .contact-list { position: absolute; left: 275px; top: 80px; font-size: 14px; color: var(--ink-soft); }
  .card-front .contact-list li { gap: 10px; height: 28px; }
  .card-front .icon { width: 14px; height: 14px; }

  /* Letterhead */
  .letterhead { position: absolute; left: 120px; top: 927px; width: 958px; height: 1245px; background: var(--paper); box-shadow: -18px 22px 40px var(--shadow); overflow: hidden; }
  .letterhead-band { position: absolute; left: 0; top: 0; width: 100%; height: 409px; background: linear-gradient(180deg, var(--band-top), var(--band-bottom)); }
  .letterhead-body-tint { position: absolute; left: 0; top: 409px; width: 100%; height: 426px; background: linear-gradient(180deg, var(--paper-tint), #eaebec); }
  .letterhead-pattern { position: absolute; left: 0; top: 835px; width: 100%; height: 410px; background: linear-gradient(180deg, #f3f4f5, #fafafa); }
  .letterhead .wordmark { position: absolute; left: 112px; top: 225px; font-size: 64px; }
  .letterhead .wordmark-mark { width: 24px; height: 24px; }
  .letterhead-band .contact-list { position: absolute; left: 621px; top: 170px; font-size: 18px; color: var(--ink); }
  .letterhead-band .contact-list li { gap: 14px; height: 34.5px; }
  .letter-subject { position: absolute; left: 113px; top: 432px; font-size: 39px; font-weight: 400; color: var(--ink); }
  .letter-text { position: absolute; left: 113px; top: 500px; width: 733px; font-size: 16.8px; line-height: 26.4px; color: var(--ink); text-align: justify; }
  .letter-text p + p { margin-top: 12px; }
  .letter-sign { position: absolute; right: 110px; top: 1024px; text-align: right; font-size: 18px; line-height: 27px; color: var(--ink); }
  .letter-sign .web { color: var(--ink-soft); }

  /* Envelope front */
  .envelope-front { position: absolute; left: 118px; top: 2310px; width: 955px; height: 493px; background: var(--paper-tint); box-shadow: -18px 22px 40px var(--shadow); overflow: hidden; }
  .envelope-pattern { position: absolute; left: 380px; top: 0; width: 575px; height: 493px; background: linear-gradient(135deg, #ebeced, #f6f6f7); }
  .envelope-front .wordmark { position: absolute; left: 56px; top: 110px; font-size: 58px; }
  .envelope-front .wordmark-mark { width: 22px; height: 22px; }
  .envelope-front .contact-list { position: absolute; left: 56px; top: 318px; font-size: 13.5px; color: var(--ink-soft); }
  .envelope-front .contact-list li { gap: 12px; height: 28.5px; }
  .envelope-front .icon { width: 16px; height: 16px; }
  .envelope-window { position: absolute; left: 452px; top: 243px; width: 418px; height: 182px; border-radius: 12px; background: linear-gradient(160deg, #e8e8e8, #bdbdbd 45%, #ececec 60%, #c6c6c6); box-shadow: inset 0 0 0 1px #c8c8c8; }

  /* Envelope back */
  .envelope-back { position: absolute; left: 122px; top: 2912px; width: 954px; height: 623px; box-shadow: -18px 22px 40px var(--shadow); }
  .envelope-back svg { display: block; }
</style>
</head>
<body>

<svg width="0" height="0" style="position:absolute" aria-hidden="true">
  <symbol id="icon-phone" viewBox="0 0 24 24"><path d="M6.6 2.5l3 3.2-1.9 2.3c1.2 2.6 3.4 4.9 6.1 6.2l2.3-1.9 3.3 3-1.6 3.4C10.3 18.6 5.2 13.6 3.3 4.2z"/></symbol>
  <symbol id="icon-globe" viewBox="0 0 24 24"><path d="M12 2a10 10 0 100 20 10 10 0 000-20zm0 2c.9 0 2.1 1.8 2.6 5H9.4C9.9 5.8 11.1 4 12 4zM4.3 11h3c0 .7 0 1.4.1 2H4.3a8 8 0 010-2zm1 4h2.4c.3 1.3.7 2.4 1.2 3.3A8 8 0 015.3 15zm2.4-6H5.3a8 8 0 013.6-3.3c-.5.9-.9 2-1.2 3.3zM12 20c-.9 0-2.1-1.8-2.6-5h5.2c-.5 3.2-1.7 5-2.6 5zm-2.8-7a19 19 0 010-2h5.6a19 19 0 010 2zm5.9 5.3c.5-.9.9-2 1.2-3.3h2.4a8 8 0 01-3.6 3.3zM16.6 13c.1-.6.1-1.3.1-2h3a8 8 0 010 2zm-.3-4c-.3-1.3-.7-2.4-1.2-3.3A8 8 0 0118.7 9z"/></symbol>
  <symbol id="icon-mail" viewBox="0 0 24 24"><path d="M2 5h20v14H2zm2 2v.4l8 5.4 8-5.4V7z"/></symbol>
  <symbol id="icon-pin" viewBox="0 0 24 24"><path d="M12 1.5a7 7 0 00-7 7c0 5 7 12 7 12s7-7 7-12a7 7 0 00-7-7zm0 4a3 3 0 110 6 3 3 0 010-6zM4 21h16v1.8H4z"/></symbol>
</svg>

<section class="card-stage" aria-label="Business cards">
  <div class="card card-front">
    <div class="card-name">Name Here</div>
    <div class="card-role">Position here</div>
    <div class="card-divider"></div>
    <ul class="contact-list">
      <li><svg class="icon"><use href="#icon-phone"/></svg>+1 234 567 890</li>
      <li><svg class="icon"><use href="#icon-globe"/></svg>www.yourwebsite.com</li>
      <li><svg class="icon"><use href="#icon-mail"/></svg>addyouremail@here.com</li>
      <li><svg class="icon"><use href="#icon-pin"/></svg>Add your location here</li>
    </ul>
  </div>
  <div class="card card-back">
    <div class="wordmark">brivora<span class="wordmark-mark"></span></div>
  </div>
</section>

<section class="letterhead" aria-label="Letterhead">
  <div class="letterhead-band">
    <div class="wordmark">brivora<span class="wordmark-mark"></span></div>
    <ul class="contact-list">
      <li><svg class="icon"><use href="#icon-phone"/></svg>+1 234 567 890</li>
      <li><svg class="icon"><use href="#icon-globe"/></svg>www.yourwebsite.com</li>
      <li><svg class="icon"><use href="#icon-mail"/></svg>addyouremail@here.com</li>
      <li><svg class="icon"><use href="#icon-pin"/></svg>Add your location here</li>
    </ul>
  </div>
  <div class="letterhead-body-tint"></div>
  <div class="letterhead-pattern" role="img" aria-label="Faint decorative pattern of rounded squares"></div>
  <h1 class="letter-subject">Subject Headline Here</h1>
  <div class="letter-text">
    <p>Lorem ipsum dolor sit amet, consectetuer adipiscing elit, sed diam nonummy nibh euismod tincidunt ut laoreet dolore magna aliquam erat volutpat. Ut wisi enim ad minim veniam, quis nostrud exerci tation ullamcorper suscipit lobortis nisl ut aliquip ex ea commodo consequat. Duis autem vel eum iriure dolor in hendrerit in vulputate velit esse molestie consequat, vel illum dolore eu feugiat nulla facilisis at vero eros et accumsan et iusto odio dignissim qui blandit praesent luptatum zzril delenit augue duis dolore te feugait nulla facilisi.</p>
    <p>Porem ipsum dolor sit amet, cons ectetuer adipiscing elit, sed diam nonummy nibh euismod tincidunt ut laoreet dolore magna aliquam erat volutpat. Ut wisi enim ad minim veniam, quis nostrud exerci tation.</p>
    <p>Lorem ipsum dolor sit amet, cons ectetuer adipiscing elit, sed diam nonummy nibh euismod tincidunt ut laoreet dolore magna aliquam erat volutpat. Ut wisi enim ad minim veniam, quis nostrud exerci tation ullamcorper suscipit lobortis nisl ut aliquip ex ea commodo consequat. Lorem ipsum dolor sit amet, cons ectetuer adipiscing elit, sed diam nonummy nibh euismod tincidunt ut laoreet dolore</p>
  </div>
  <div class="letter-sign">
    <div>Add your name and position here</div>
    <div>Lorem ipsum dolor sit amet</div>
    <div class="web">www.yourwebsite.com</div>
  </div>
</section>

<section class="envelope-front" aria-label="Envelope front">
  <div class="envelope-pattern" role="img" aria-label="Faint decorative pattern of rounded squares"></div>
  <div class="wordmark">brivora<span class="wordmark-mark"></span></div>
  <ul class="contact-list">
    <li><svg class="icon"><use href="#icon-phone"/></svg>+1 234 567 890</li>
    <li><svg class="icon"><use href="#icon-globe"/></svg>www.yourwebsite.com</li>
    <li><svg class="icon"><use href="#icon-mail"/></svg>addyouremail@here.com</li>
    <li><svg class="icon"><use href="#icon-pin"/></svg>Add your location here</li>
  </ul>
  <div class="envelope-window"></div>
</section>

<section class="envelope-back" aria-label="Envelope back">
  <svg width="954" height="623" viewBox="0 0 954 623">
    <defs>
      <linearGradient id="flap-outer" x1="0" y1="0" x2="0" y2="1">
        <stop offset="0" stop-color="#f1f1f1"/><stop offset="1" stop-color="#d9d9d9"/>
      </linearGradient>
      <linearGradient id="flap-inner" x1="0" y1="0" x2="0" y2="1">
        <stop offset="0" stop-color="#d0d0d0"/><stop offset="1" stop-color="#f2f2f2"/>
      </linearGradient>
      <linearGradient id="env-body" x1="0" y1="0" x2="0" y2="1">
        <stop offset="0" stop-color="#f7f7f7"/><stop offset="1" stop-color="#ffffff"/>
      </linearGradient>
    </defs>
    <path d="M70 0 H884 Q930 0 950 55 L954 130 H0 L8 65 Q30 0 70 0 Z" fill="url(#flap-outer)"/>
    <rect x="0" y="130" width="954" height="493" fill="url(#env-body)"/>
    <path d="M0 130 H954 L900 238 Q880 275 830 275 H124 Q74 275 54 238 Z" fill="url(#flap-inner)"/>
  </svg>
</section>

</body>
</html>
```